Saffron Ledger Works Flyer

We need a one page promotional piece that explains what our company does, and the benefits it provides in a simple, elegant, easy to understand way. I would like to print it on glossy heavyweight paper to give a feel of high quality and legitimacy. I will include the logo, the tag line, and the main benefits that the company offers.

Tag line concept, may not need these exact words. "Give us 5 minutes a day, and we will help you build a Saffron Ledger Works."

Key points...(exact wording not required if you think of a better way to say it)

Software easy enough for my grandpa to use.
Lets you use snail mail, email, texting, and social media to quickly market to your customers at very low cost.
Web based which allows you to launch media campaigns from your desktop, or smartphone in moments.
Quick 3 - 5 minute training videos which give you hard hitting, quick action tips that will help you make your business better today.
Live coaching calls to help motivate you to improve your business.
No contracts, or start up fees. One low price of $299 per month.

Restaurant owners

Restaurant

```html
<!DOCTYPE html>
<html lang="en">
<head>
<meta charset="utf-8">
<title>Saffron Ledger Works Flyer</title>
<link rel="stylesheet" href="https://fonts.googleapis.com/css2?family=Aleo:ital,wght@0,400;0,700;1,400&family=Lato:ital,wght@0,400;0,700;0,900;1,400&display=swap">
<style>
  :root {
    --page-bg: #ececec;
    --paper: #ffffff;
    --green: #52a23a;
    --panel-green: rgba(104, 156, 58, 0.88);
    --grey-text: #5c5c5c;
    --body-text: #4a4a4a;
    --photo-dark: #2a1d16;
    --photo-warm: #8a6a45;
  }
  * { margin: 0; padding: 0; box-sizing: border-box; }
  html, body { width: 1200px; height: 857px; overflow: hidden; }
  body { background: var(--page-bg); position: relative; font-family: "Lato", sans-serif; }

  .flyer {
    position: absolute; left: 327px; top: 18px; width: 576px; height: 812px;
    background: var(--paper);
    box-shadow: 0 2px 6px rgba(0,0,0,0.15);
  }
  .brand {
    position: absolute; left: 0; top: 0; width: 100%; height: 106px;
    display: flex; align-items: center; justify-content: center; gap: 12px;
  }
  .brand-mark { width: 18px; height: 18px; border-radius: 50%; background: var(--green); }
  .brand-name {
    font-family: "Aleo", serif; font-weight: 700; font-size: 34px; color: var(--green);
  }

  .hero-photo {
    position: absolute; left: 0; top: 106px; width: 576px; height: 366px;
    background: linear-gradient(160deg, var(--photo-dark) 0%, #4a3426 40%, var(--photo-warm) 70%, #c9b48a 100%);
  }
  .hero-panel {
    position: absolute; left: 323px; top: 106px; width: 240px; height: 388px;
    background: var(--panel-green); color: #fff; text-align: center;
    padding-top: 16px;
  }
  .hero-panel .lead { font-family: "Aleo", serif; font-style: italic; font-size: 32px; line-height: 1.1; }
  .hero-panel .big { font-weight: 700; font-size: 64px; line-height: 0.98; letter-spacing: -1px; margin-top: 4px; }
  .hero-panel .mid { font-weight: 700; font-size: 31px; line-height: 1.05; margin-top: 6px; }
  .hero-panel .mid.large { font-size: 38px; margin-top: 0; }
  .hero-panel .promise {
    display: inline-block; background: #fff; color: var(--green);
    font-weight: 700; font-size: 19px; line-height: 1.1; padding: 3px 6px; margin-top: 10px;
    border: 2px solid #fff;
  }
  .hero-panel .url { font-weight: 700; font-size: 17px; margin-top: 14px; }

  .pricing { position: absolute; left: 0; top: 496px; width: 100%; text-align: center; font-family: "Aleo", serif; font-weight: 700; }
  .pricing .terms { color: var(--grey-text); font-size: 27px; }
  .pricing .price { color: var(--green); font-size: 27px; margin-top: 2px; }

  .benefits { position: absolute; left: 28px; top: 574px; width: 530px; list-style: none; }
  .benefits li {
    display: flex; gap: 8px; align-items: flex-start;
    font-style: italic; font-size: 12.5px; line-height: 15px; color: var(--body-text);
    margin-bottom: 9px;
  }
  .benefits svg { flex: 0 0 20px; width: 20px; height: 20px; }

  .footer-url { position: absolute; left: 40px; top: 761px; color: var(--green); font-size: 13px; letter-spacing: 0.5px; }
  .footer-phone { position: absolute; right: 22px; top: 747px; display: flex; align-items: center; gap: 10px; color: var(--green); font-weight: 700; font-size: 28px; }
  .footer-phone svg { width: 38px; height: 38px; }
  .footer-band { position: absolute; left: 0; bottom: 0; width: 100%; height: 14px; background: var(--green); }
</style>
</head>
<body>
  <main class="flyer">
    <header class="brand">
      <span class="brand-mark"></span>
      <span class="brand-name">Saffron Ledger Works</span>
    </header>

    <div class="hero-photo" role="img" aria-label="Photograph of a modern restaurant bar with stools, shelves of bottles and cocktails on the counter"></div>

    <section class="hero-panel">
      <p class="lead">Give us</p>
      <p class="big">5 MIN<br>A DAY</p>
      <p class="mid">AND WE WILL</p>
      <p class="mid large">HELP YOU</p>
      <p class="promise">BUILD A SAFFRON<br>LEDGER WORKS</p>
      <p class="url">www.saffronledgerworks.com</p>
    </section>

    <section class="pricing">
      <p class="terms">No contracts, or start up fees</p>
      <p class="price">One low price of $299 per month</p>
    </section>

    <ul class="benefits">
      <li><svg viewBox="0 0 20 20"><rect width="20" height="20" rx="2" fill="#52a23a"/><path d="M4.5 10.5l3.5 3.5 7.5-8" fill="none" stroke="#fff" stroke-width="2.6" stroke-linecap="round" stroke-linejoin="round"/></svg><span>Software easy enough for your grandpa to use.</span></li>
      <li><svg viewBox="0 0 20 20"><rect width="20" height="20" rx="2" fill="#52a23a"/><path d="M4.5 10.5l3.5 3.5 7.5-8" fill="none" stroke="#fff" stroke-width="2.6" stroke-linecap="round" stroke-linejoin="round"/></svg><span>Lets you use snail mail, email, texting, and social media to quickly market to your customers at very low cost.</span></li>
      <li><svg viewBox="0 0 20 20"><rect width="20" height="20" rx="2" fill="#52a23a"/><path d="M4.5 10.5l3.5 3.5 7.5-8" fill="none" stroke="#fff" stroke-width="2.6" stroke-linecap="round" stroke-linejoin="round"/></svg><span>Web based which allows you to launch media campaigns from your desktop, or smartphone in moments.</span></li>
      <li><svg viewBox="0 0 20 20"><rect width="20" height="20" rx="2" fill="#52a23a"/><path d="M4.5 10.5l3.5 3.5 7.5-8" fill="none" stroke="#fff" stroke-width="2.6" stroke-linecap="round" stroke-linejoin="round"/></svg><span>Quick 3 - 5 minute training videos which give you hard hitting, quick action tips that will help you make your business better today.</span></li>
      <li><svg viewBox="0 0 20 20"><rect width="20" height="20" rx="2" fill="#52a23a"/><path d="M4.5 10.5l3.5 3.5 7.5-8" fill="none" stroke="#fff" stroke-width="2.6" stroke-linecap="round" stroke-linejoin="round"/></svg><span>Live coaching calls to help motivate you to improve your business.</span></li>
    </ul>

    <p class="footer-url">WWW.SAFFRONLEDGERWORKS.COM</p>
    <div class="footer-phone">
      <svg viewBox="0 0 38 38" aria-hidden="true"><rect width="38" height="38" rx="3" fill="#52a23a"/><path d="M8 15c0-4 5-6 11-6s11 2 11 6v2h-6v-3h-10v3H8z" fill="#fff"/><rect x="10" y="19" width="18" height="11" rx="2" fill="#fff"/><g fill="#52a23a"><circle cx="15" cy="22.5" r="1.2"/><circle cx="19" cy="22.5" r="1.2"/><circle cx="23" cy="22.5" r="1.2"/><circle cx="15" cy="26.5" r="1.2"/><circle cx="19" cy="26.5" r="1.2"/><circle cx="23" cy="26.5" r="1.2"/></g></svg>
      <span>014-275-390</span>
    </div>
    <div class="footer-band"></div>
  </main>
</body>
</html>
```